Gutschein-Design für Bauträgerfirma
Sehr guter Designer, würde ich immer wieder weiter empfehlen.
Zielgruppe
Wir sind eine Bauträgerfirma und verkaufen Wohnungen für die gehobene Klasse.
Aufgabenstellung
Auflösung min. 150dpi, Format: 3,56m x 2,52m,
Dieses Banner soll eine Werbung bzw. einen Gutschein enthalten.
Folgender Text soll enthalten sein: Wenn Sie eine Wohnung bis zum 31.12.2018 bei uns kaufen, erhalten Sie einen Bemusterungsgutschein von 5.000€.
Der Text kann natürlich auch anders formuliert werden, der Kern sollte erhalten bleiben.
Die Unterlagen können auch im anderen Format zur Verfügung gestellt werden. Es sind alle Render in großem Format verfügbar.

```html
<!DOCTYPE html>
<html lang="de">
<head>
<meta charset="utf-8">
<title>Halden Wohnbau – Bemusterungsgutschein</title>
<link rel="stylesheet" href="https://fonts.googleapis.com/css2?family=Open+Sans:wght@400;600&display=swap">
<style>
  :root {
    --navy: #142d5a;
    --navy-deep: #10264e;
    --haze: #dcdcda;
    --mist: #a7a8ad;
    --dusk: #5f6381;
    --white: #ffffff;
    --stage: #e8eaed;
  }
  * { margin: 0; padding: 0; box-sizing: border-box; }
  html, body {
    width: 1200px;
    height: 965px;
    overflow: hidden;
    background: var(--stage);
    font-family: "Open Sans", Arial, sans-serif;
  }
  .banner {
    position: absolute;
    left: 40px;
    top: 86px;
    width: 1120px;
    height: 793px;
    background: var(--navy);
    overflow: hidden;
  }
  .banner__photo {
    position: absolute;
    inset: 0 0 auto 0;
    height: 520px;
    background: linear-gradient(180deg,
      var(--haze) 0%,
      var(--mist) 28%,
      var(--dusk) 55%,
      var(--navy) 100%);
  }
  .offer-band {
    position: absolute;
    left: 0;
    width: 74%;
    background: var(--white);
    color: var(--navy);
    text-transform: uppercase;
    font-weight: 400;
    font-size: 36px;
    letter-spacing: 0.5px;
    line-height: 1.2;
    padding-left: 44px;
    display: flex;
    flex-direction: column;
    justify-content: center;
  }
  .offer-band--question { top: 96px; height: 74px; }
  .offer-band--reward { top: 196px; height: 156px; }
  .brand {
    position: absolute;
    left: 70px;
    top: 560px;
    display: flex;
    align-items: center;
    gap: 16px;
    color: var(--white);
  }
  .brand__mark {
    width: 22px;
    height: 22px;
    background: var(--white);
  }
  .brand__name {
    font-size: 42px;
    font-weight: 400;
    letter-spacing: 1px;
  }
  .benefits {
    position: absolute;
    left: 51%;
    top: 412px;
    list-style: none;
    color: var(--white);
    text-transform: uppercase;
    font-size: 27px;
    line-height: 1.42;
    letter-spacing: 0.3px;
  }
  .benefits li::before {
    content: "•";
    margin-right: 10px;
  }
  .contact-strip {
    position: absolute;
    left: 0;
    right: 0;
    bottom: 0;
    height: 92px;
    background: var(--white);
    color: var(--navy);
    display: flex;
    align-items: center;
    justify-content: center;
    font-size: 28px;
    text-transform: uppercase;
    letter-spacing: 0.4px;
  }
  .contact-strip__sep { margin: 0 12px; }
</style>
</head>
<body>
  <main class="banner">
    <div class="banner__photo" role="img" aria-label="Luftaufnahme einer Stadt mit Feldern im Dunst, nach unten in Dunkelblau übergehend"></div>

    <p class="offer-band offer-band--question">Sie kaufen eine Wohnung bis zum 31.12.2018?</p>
    <p class="offer-band offer-band--reward">
      <span>Dann erhalten Sie einen</span>
      <span>Bemusterungsgutschein im Wert von 5.000€!</span>
    </p>

    <div class="brand">
      <span class="brand__mark"></span>
      <span class="brand__name">HALDEN WOHNBAU</span>
    </div>

    <ul class="benefits">
      <li>Hochmoderne Architektur</li>
      <li>Top-Lagen</li>
      <li>Hochwertige Ausstattung</li>
      <li>Faires Preis-Leistungsverhältnis</li>
      <li>Überzeugende Qualität</li>
    </ul>

    <footer class="contact-strip">
      <span>Telefon: 07351/218 46 90</span>
      <span class="contact-strip__sep">•</span>
      <span>halden-wohnbau.de</span>
    </footer>
  </main>
</body>
</html>
```